ARC VOLLEY Business Card Project

I'd like to request a business card design for the new company I've launched.
The name of the company is "ARC VOLLEY" an indoor unmanned tennis practice facility.
We would like to see designs that use our brand identity color in the logo I've attached.
We hope to get the design with modern, luxurious and elegant tone and manner.
We hope the logo should not be too big.

Business card must have elements as below:
- Logo (One of the logos I've attached)
- Name (In Korean Text) : 박 서 윤
- Title (In Korean Text) : 대표
- Phone Number : 010-8472-3916
- Email Address : seoyun.park@arcvolley-example.co.kr
- Website : www.arcvolley-example.co.kr
- Instagram : arcvolley
- Address (In Korean text) : 경기도 용인시 수지구 풍덕천로 456 미래타워 5층 501호, 502호

Target Market(s)

Tennis amateurs in 20 to 40s

Industry/Entity Type

Sports, Hobby

Contact Information for Business Card

- Logo (One of the logos I've attached) - Name (In Korean Text) : 박 서 윤 - Title (In Korean Text) : 대표 - Phone Number : 010-8472-3916 - Email Address : seoyun.park@arcvolley-example.co.kr - Website : www.arcvolley-example.co.kr - Instagram : arcvolley - Address (In Korean text) : 경기도 용인시 수지구 풍덕천로 456 미래타워 5층 501호, 502호

Font styles to use
Sans Serif

Requirements
Must have
• Double sided
Nice to have
• Logo with intaglio or relief embossing
Should not have
• Logo should not be too big.

```html
<!DOCTYPE html>
<html lang="ko">
<head>
<meta charset="utf-8">
<title>ARC VOLLEY — Business Card</title>
<link href="https://fonts.googleapis.com/css2?family=Montserrat:wght@400;500&family=Noto+Sans+KR:wght@400;500&display=swap" rel="stylesheet">
<style>
  :root {
    --backdrop: #c8c9ca;
    --paper: #f3f2ee;
    --brand-green: #1f4a2b;
    --brand-green-deep: #183d23;
    --ink-grey: #6e6f70;
    --rule: #8a8b8b;
    --on-green: #f2f1ec;
  }
  * { margin: 0; padding: 0; box-sizing: border-box; }
  html, body {
    width: 1200px;
    height: 794px;
    overflow: hidden;
    background: var(--backdrop);
  }
  .sheet {
    position: relative;
    width: 1200px;
    height: 794px;
    display: flex;
    align-items: center;
    justify-content: center;
    gap: 60px;
  }
  .card {
    position: relative;
    width: 520px;
    height: 298px;
    border-radius: 3px;
    box-shadow: 0 10px 24px rgba(0, 0, 0, 0.14), 0 2px 5px rgba(0, 0, 0, 0.08);
  }

  /* Front side */
  .card--front {
    background: var(--paper);
    border-bottom: 2px solid var(--brand-green);
  }
  .front-logo {
    position: absolute;
    left: 44px;
    top: 134px;
    font-family: "Montserrat", sans-serif;
    font-weight: 500;
    font-size: 20px;
    letter-spacing: 0.08em;
    color: var(--brand-green);
    white-space: nowrap;
  }
  .divider {
    position: absolute;
    left: 222px;
    top: 62px;
    width: 1px;
    height: 172px;
    background: var(--rule);
  }
  .details {
    position: absolute;
    left: 238px;
    top: 58px;
    width: 264px;
  }
  .person-name {
    font-family: "Noto Sans KR", sans-serif;
    font-weight: 400;
    font-size: 19px;
    letter-spacing: 0.12em;
    color: var(--brand-green);
    line-height: 1.2;
  }
  .person-title {
    font-family: "Noto Sans KR", sans-serif;
    font-weight: 400;
    font-size: 11px;
    color: var(--brand-green);
    margin-top: 2px;
  }
  .contact {
    margin-top: 12px;
    font-family: "Montserrat", sans-serif;
    font-weight: 400;
    font-size: 10.5px;
    line-height: 1.6;
    color: var(--ink-grey);
    list-style: none;
    white-space: nowrap;
  }
  .contact .label {
    display: inline-block;
    width: 22px;
    font-weight: 500;
    color: var(--brand-green);
  }
  .contact .address {
    margin-top: 4px;
    font-family: "Noto Sans KR", sans-serif;
    font-size: 10px;
    line-height: 1.6;
    white-space: normal;
  }

  /* Back side */
  .card--back {
    background: var(--brand-green);
    border-bottom: 2px solid var(--brand-green-deep);
    display: flex;
    align-items: center;
    justify-content: center;
  }
  .back-logo {
    font-family: "Montserrat", sans-serif;
    font-weight: 500;
    font-size: 38px;
    letter-spacing: 0.08em;
    color: var(--on-green);
    white-space: nowrap;
  }
</style>
</head>
<body>
  <main class="sheet">
    <section class="card card--front" aria-label="Business card, front">
      <div class="front-logo">ARC VOLLEY</div>
      <div class="divider"></div>
      <div class="details">
        <p class="person-name">박 서 윤</p>
        <p class="person-title">대표</p>
        <ul class="contact">
          <li><span class="label">T</span>010-8472-3916</li>
          <li><span class="label">E</span>seoyun.park@arcvolley-example.co.kr</li>
          <li><span class="label">W</span>www.arcvolley-example.co.kr</li>
          <li><span class="label">IG</span>arcvolley</li>
          <li class="address">경기도 용인시 수지구 풍덕천로 456<br>미래타워 5층 501호, 502호</li>
        </ul>
      </div>
    </section>

    <section class="card card--back" aria-label="Business card, back">
      <div class="back-logo">ARC VOLLEY</div>
    </section>
  </main>
</body>
</html>
```